Professional, Attractive, Simple Website Needed!!

We completed the design for our logo.

We need a website built out around this.

Here are a couple samples of how we want ours formatted.

http://brvntapower.com

http://www.halvorbeam.com/lp/free-quote?LeadSource=Search%20Engine&ProgramName=webquery&experience=qual&language=en&type=brd&gclid=Xq7RTPwmEYKDLAvUHbsNQkfPZrTcGwnJuoVbXeLqHmRYdAsWtPkMcNfBYgzTrUoQJhEdWvKpYaLsZbCmNDgQwTxAoKpXbT_qkR

http://morvalo.co

Reason: Extending this deadline due to our delay in providing designers with content for each page. This is coming in next 24 hours.

Reason: Due to scheduling conflicts and extended travel delays related to Puerto Rico, the deadline has been extended. Your patience is greatly appreciated.

Reason: Travel and scheduling conflicts have made it impossible to give this project the thorough review it deserves, therefore I am extending the deadline. Thank you for your patience!

Target Market(s)

Home Owners who earn 60k + household annually

Industry/Entity Type

It Professional

Coding

Coded - Design and coding required

Number of Pages Required

5+ page

Font styles to use
Serif

Colors
34a7d8
9bcb3c

Requirements
Must have
• Simple
• Lead form Entry (Ability for visitor to enter Name, number and address for a quote)
• Sleek Design
• Professional
• Testimonials
• Use color Scheme of Design Logo Attached
Nice to have
• Video when site starts
• Like this
• https://www.vidmarrow.com/watch?v=qT8mRpXw2Ka&feature=vidm.ro
Should not have
• Should not include Commercial solar
• Should not include wind power

```html
<!DOCTYPE html>
<html lang="en">
<head>
<meta charset="utf-8">
<title>Sunward Energy — Residential Solar</title>
<link href="https://fonts.googleapis.com/css2?family=Montserrat:wght@400;600;700&family=Open+Sans:wght@400;600&display=swap" rel="stylesheet">
<style>
:root{
  --green:#8cc63f;
  --green-deep:#5aa532;
  --lime:#c5d82b;
  --blue:#34a7d8;
  --ink:#2b2b2b;
  --muted:#9a9a9a;
  --pale:#f4f7f9;
  --white:#ffffff;
  --col1:#bdd42a;
  --col2:#98c21f;
  --col3:#6db13c;
  --col4:#469a3d;
}
*{box-sizing:border-box;margin:0;padding:0}
html,body{width:1200px;height:3629px;overflow:hidden}
body{position:relative;background:var(--white);font-family:"Open Sans",Arial,sans-serif;color:var(--ink)}
.abs{position:absolute}
h1,h2,h3,h4,.nav,.btn{font-family:"Montserrat",Arial,sans-serif}

.topbar{left:0;top:0;width:1200px;height:24px;background:var(--green);color:#fff;font-size:10px;display:flex;align-items:center;justify-content:space-between;padding:0 72px}
.topbar .dots{display:flex;gap:6px}
.topbar .dots i{width:10px;height:10px;border-radius:50%;background:rgba(255,255,255,.85);display:block}

.header{left:0;top:24px;width:1200px;height:76px;background:#fff}
.brand{left:109px;top:40px;display:flex;align-items:center;gap:8px;font-family:"Montserrat",sans-serif;font-weight:700;font-size:17px;color:var(--blue)}
.brand i{width:26px;height:26px;border-radius:50%;background:var(--green);display:block}
.nav{left:733px;top:54px;display:flex;gap:30px;font-size:11px;color:#555;letter-spacing:.3px}
.nav .active{color:var(--green);border-bottom:2px solid var(--green);padding-bottom:4px}

.hero{left:0;top:100px;width:1200px;height:428px;background:linear-gradient(90deg,#f6f7f8 0%,#eef0f2 45%,#e8ebee 100%)}
.hero-photo{left:557px;top:100px;width:643px;height:428px;background:linear-gradient(135deg,#dfe4ea 0%,#8ec3ea 30%,#3f8fd6 60%,#cfd6dd 100%)}
.quote{left:138px;top:194px;width:368px;height:194px;background:#fff;border:4px solid var(--green);border-radius:8px}
.quote h3{background:var(--blue);color:#fff;text-align:center;font-size:17px;font-weight:700;height:32px;line-height:32px;margin:0 -1px}
.quote .field{position:absolute;left:90px;width:224px;height:20px;border:1px solid #9a9a9a;font-size:10px;color:#666;padding:2px 6px}
.btn{display:inline-flex;align-items:center;justify-content:center;border-radius:20px;font-size:9px;font-weight:600;letter-spacing:.4px}
.btn-outline{border:1px solid #c9c9c9;color:#555;background:#fff}
.btn-green{background:var(--green);color:#fff}
.slider-dots{left:165px;top:468px;display:flex;gap:6px}
.slider-dots i{width:6px;height:6px;border-radius:50%;background:#999;display:block}
.slider-dots i.on{background:#444}

.features{left:0;top:528px;width:1200px;height:382px;display:flex}
.feature{width:300px;height:382px;color:#fff;text-align:center;position:relative}
.feature svg{position:absolute;left:118px;top:96px}
.feature .num{position:absolute;top:724px;width:100%;font-size:9px;opacity:.7}
.feature h4{position:absolute;top:250px;width:100%;font-size:14px;line-height:20px;font-weight:700;letter-spacing:.5px}
.feature .idx{position:absolute;top:200px;width:100%;font-size:9px;opacity:.75}

.coverage-art{left:165px;top:920px;width:312px;height:345px;background:radial-gradient(ellipse at 50% 35%,#7dc243 0%,#9b7f7a 55%,#ffffff 75%)}
.section-title{font-size:30px;font-weight:700;line-height:36px;color:var(--ink)}
.lead{font-size:11px;color:var(--muted);line-height:18px}

.why{left:0;top:1271px;width:1200px;height:377px;background:linear-gradient(100deg,#6cb530 0%,#8cc63f 60%,#9ccf3e 100%)}
.why-decor{left:680px;top:1271px;width:520px;height:377px;background:radial-gradient(ellipse at 65% 40%,#c9e040 0%,#3f9c35 30%,rgba(140,198,63,0) 60%)}
.why h2{color:#fff;font-size:29px;font-weight:700}

.testimonial{left:0;top:1648px;width:1200px;height:385px;background:var(--pale)}
.person{left:121px;top:1657px;width:351px;height:376px;background:linear-gradient(180deg,#e6d5c7 0%,#7eb8dd 55%,#4f93c8 100%)}

.chart-sec{left:0;top:2033px;width:1200px;height:677px;background:linear-gradient(180deg,#ffffff 0%,#f0f5f9 100%)}

.info{left:0;top:2710px;width:1200px;height:610px;background:#fff}
.info-photo{width:516px;height:283px}
.info h4{font-size:13px;font-weight:600;letter-spacing:.3px;color:#333}

.footer{left:0;top:3320px;width:1200px;height:309px;background:linear-gradient(180deg,#7fc23a 0%,#66b42f 100%);color:#fff}
.badge{width:155px;height:62px;background:#fff;border-radius:6px}
.flinks{list-style:none;font-size:10px;line-height:29px;font-family:"Montserrat",sans-serif}
.totop{width:36px;height:36px;border-radius:50%;background:var(--green);display:flex;align-items:center;justify-content:center}
</style>
</head>
<body>

<div class="abs topbar"><span>Call Us Now: 555 214 6093</span><span class="dots"><i></i><i></i><i></i><i></i><i></i></span></div>

<header class="abs header"></header>
<div class="abs brand"><i></i>Sunward Energy</div>
<nav class="abs nav"><span class="active">HOME</span><span>PRODUCTS</span><span>SERVICES</span><span>BLOG</span><span>CONTACTS</span><span>PAGES</span></nav>

<section class="abs hero"></section>
<div class="abs hero-photo" role="img" aria-label="Rooftop solar panel array against a pale sky"></div>
<form class="abs quote">
  <h3>Get A Instant Quote</h3>
  <div class="field" style="top:44px">Name</div>
  <div class="field" style="top:68px">Email</div>
  <div class="field" style="top:92px">Phone#</div>
  <span class="abs btn btn-outline" style="left:23px;top:142px;width:140px;height:36px">FIND OUT MORE</span>
  <span class="abs btn btn-green" style="left:178px;top:142px;width:130px;height:36px">Get My Quote →</span>
</form>
<div class="abs slider-dots"><i></i><i class="on"></i><i></i></div>

<section class="abs features">
  <div class="feature" style="background:var(--col1)">
    <svg width="64" height="72" viewBox="0 0 64 72" fill="none" stroke="#fff" stroke-width="3"><rect x="6" y="2" width="52" height="68" rx="4"/><line x1="16" y1="18" x2="48" y2="18"/><line x1="16" y1="36" x2="26" y2="36"/><line x1="21" y1="31" x2="21" y2="41"/><line x1="38" y1="36" x2="48" y2="36"/><line x1="17" y1="50" x2="25" y2="58"/><line x1="25" y1="50" x2="17" y2="58"/><line x1="38" y1="52" x2="48" y2="52"/><line x1="38" y1="57" x2="48" y2="57"/></svg>
    <div class="idx">001</div><h4>CALCULATE MY<br>SAVINGS WITH<br>SOLAR</h4>
  </div>
  <div class="feature" style="background:var(--col2)">
    <svg width="64" height="72" viewBox="0 0 64 72" fill="none" stroke="#fff" stroke-width="3"><circle cx="32" cy="36" r="12"/><line x1="32" y1="6" x2="32" y2="16"/><line x1="32" y1="56" x2="32" y2="66"/><line x1="2" y1="36" x2="12" y2="36"/><line x1="52" y1="36" x2="62" y2="36"/><line x1="11" y1="15" x2="18" y2="22"/><line x1="46" y1="50" x2="53" y2="57"/><line x1="53" y1="15" x2="46" y2="22"/><line x1="18" y1="50" x2="11" y2="57"/></svg>
    <div class="idx">002</div><h4>INSTALLATION:<br>HOW IT<br>WORKS?</h4>
  </div>
  <div class="feature" style="background:var(--col3)">
    <svg width="64" height="72" viewBox="0 0 64 72" fill="none" stroke="#fff" stroke-width="3"><path d="M10 2h32l14 14v54H10z"/><path d="M42 2v14h14"/><line x1="20" y1="30" x2="46" y2="30"/><line x1="20" y1="40" x2="46" y2="40"/><line x1="20" y1="50" x2="46" y2="50"/><line x1="20" y1="60" x2="38" y2="60"/></svg>
    <div class="idx">003</div><h4>OUR<br>WARRANTIES<br>POLICY</h4>
  </div>
  <div class="feature" style="background:var(--col4)">
    <svg width="64" height="72" viewBox="0 0 64 72" fill="none" stroke="#fff" stroke-width="3"><path d="M30 22a16 16 0 1 0 4 26"/><path d="M24 14l8 8-8 8"/><path d="M34 50a16 16 0 1 0-4-26"/><path d="M40 58l-8-8 8-8"/></svg>
    <div class="idx">004</div><h4>ADDITIONAL<br>POWER TO<br>YOUR SOLAR</h4>
  </div>
</section>

<div class="abs coverage-art" role="img" aria-label="Illustration of a floating low-poly island with trees and a wind-free rocky base"></div>
<h2 class="abs section-title" style="left:612px;top:1008px">Our Coverage Is<br>the Best In the Industry</h2>
<p class="abs lead" style="left:612px;top:1093px">with repairs and a production guarantee at no additional charge.</p>
<span class="abs btn btn-outline" style="left:612px;top:1132px;width:138px;height:32px">GET A QUOTE</span>

<section class="abs why"></section>
<div class="abs why-decor" role="img" aria-label="Decorative green and yellow ribbon swirl"></div>
<h2 class="abs" style="left:111px;top:1389px;color:#fff;font-size:29px;font-weight:700;font-family:Montserrat,sans-serif">Why Brightfield?</h2>
<p class="abs" style="left:111px;top:1438px;width:460px;color:#fff;font-size:11px;line-height:17px;opacity:.9">After years of experience and more than 500,000 people powered with the help of our solar panels, we think the choice is really obvious here!</p>
<span class="abs btn" style="left:111px;top:1505px;width:199px;height:34px;border:1px solid #fff;color:#fff">FIND OUT MORE ABOUT US</span>

<section class="abs testimonial"></section>
<div class="abs person" role="img" aria-label="Photo of a smiling customer giving a thumbs up"></div>
<h2 class="abs section-title" style="left:612px;top:1782px">Our Customers Enjoy</h2>
<p class="abs" style="left:612px;top:1824px;font-size:12px;font-weight:600;color:#555;font-family:Montserrat,sans-serif">THE SUNNY SIDE OF THEIR ENERGY CONSUMPTION BILL</p>
<p class="abs lead" style="left:612px;top:1858px;width:500px">Immediately after purchasing and installing these solar panels at my home's rooftop, I've seen tremendous cuts in energy that our family consumes!</p>
<p class="abs" style="left:612px;top:1920px;font-size:13px;font-weight:600;color:var(--green)">Dalton Reyes</p>

<section class="abs chart-sec"></section>
<h3 class="abs" style="left:0;width:1200px;top:2096px;text-align:center;font-size:14px;font-weight:600;color:#444;line-height:20px">NEW COAL CAN'T DELIVER POWER FOR 6-8 YEARS,<br>WHILE SOLAR WILL BE COMPETITIVE</h3>
<svg class="abs" style="left:0;top:2140px" width="1200" height="520" viewBox="0 2140 1200 520" font-family="Open Sans,sans-serif" font-size="9" fill="#777">
  <line x1="152" y1="2531" x2="1011" y2="2531" stroke="#ccc"/>
  <line x1="152" y1="2168" x2="152" y2="2531" stroke="#e3e3e3"/>
  <text x="118" y="2171">$0.11</text><text x="118" y="2350">$0.08</text><text x="130" y="2534">$0</text>
  <text x="100" y="2400" transform="rotate(-90 100 2400)">Cents per kilowatt hour</text>
  <path d="M600 2425 L1011 2268 L1011 2531 L600 2531Z" fill="#d7e6ee" opacity=".8"/>
  <path d="M600 2425 L1011 2350 L1011 2531 L600 2531Z" fill="#bcd4df" opacity=".7"/>
  <path d="M152 2168 L430 2318 L700 2395 L1011 2467 L1011 2531 L152 2531Z" fill="#8cc63f" opacity=".85"/>
  <path d="M152 2390 L430 2360 L1011 2440 L1011 2531 L152 2531Z" fill="#7ab634" opacity=".7"/>
  <g text-anchor="middle"><text x="162" y="2552">2010</text><text x="268" y="2552">2012</text><text x="375" y="2552">2014</text><text x="481" y="2552">2016</text><text x="588" y="2552">2018</text><text x="694" y="2552">2020</text><text x="800" y="2552">2022</text><text x="906" y="2552">2024</text><text x="1001" y="2552">2026</text></g>
  <rect x="155" y="2378" width="68" height="24" fill="#2f3438"/><text x="189" y="2394" fill="#fff" text-anchor="middle">$0.07</text>
  <rect x="1028" y="2234" width="72" height="26" fill="#2f3438"/><text x="1064" y="2251" fill="#fff" text-anchor="middle">$0.106</text>
  <rect x="1028" y="2336" width="72" height="24" fill="#2f3438"/><text x="1064" y="2352" fill="#fff" text-anchor="middle">$0.086</text>
  <rect x="1028" y="2372" width="72" height="24" fill="#8cc63f"/><text x="1064" y="2388" fill="#fff" text-anchor="middle">$0.07</text>
  <rect x="682" y="2610" width="14" height="14" fill="#8cc63f"/><text x="704" y="2621">Solar PV LCOE</text>
  <rect x="859" y="2610" width="14" height="14" fill="#d7e6ee"/><text x="881" y="2621">Coal Plant 5%</text><text x="881" y="2634">500 MW</text>
</svg>

<section class="abs info"></section>
<h2 class="abs" style="left:0;width:1200px;top:2784px;text-align:center;font-size:28px;font-weight:700;font-family:Montserrat,sans-serif">More Useful Info</h2>
<div class="abs info-photo" style="left:73px;top:2855px;background:linear-gradient(150deg,#e9f3fb 0%,#3d84d0 40%,#1f4f9a 100%)" role="img" aria-label="Close-up of blue solar panels under sunlight"></div>
<div class="abs info-photo" style="left:612px;top:2855px;background:linear-gradient(90deg,#5a5a5a 0%,#b9b9b9 45%,#e2e2e2 100%)" role="img" aria-label="Home battery unit charging an electric car in a garage"></div>
<h4 class="abs" style="left:73px;top:3164px;font-size:13px;font-weight:600;font-family:Montserrat,sans-serif;color:#333">WILL SOLAR PANELS LOOK GOOD ON MY ROOF?</h4>
<p class="abs lead" style="left:73px;top:3200px;width:500px">Absolutely! Our set of contemporary designed, low-profile and premium front trim panels will integrate beautifully into your home or office building's exterior, adding a stylish touch of futurism to it...</p>
<h4 class="abs" style="left:612px;top:3164px;font-size:13px;font-weight:600;font-family:Montserrat,sans-serif;color:#333">HOW DOES SOLAR POWER WORK?</h4>
<p class="abs lead" style="left:612px;top:3200px;width:500px">In short, our panels absorb the sun energy, then channelling it through discreetly placed wires to an inverter. There it is being converted to electricity which eventually powers your home.</p>

<footer class="abs footer"></footer>
<p class="abs" style="left:73px;top:3394px;width:240px;color:#fff;font-size:11px;line-height:18px">We are an environmentally conscious renewable energy company that offers the most eco-friendly, cost-efficient and high-energy generating products and solutions on the solar panels market!</p>
<div class="abs badge" style="left:341px;top:3394px"></div>
<div class="abs badge" style="left:341px;top:3467px"></div>
<ul class="abs flinks" style="left:612px;top:3391px;color:#fff"><li>HOME</li><li>PRODUCTS</li><li>SERVICES</li><li>BLOG</li><li>CONTACTS</li><li>PAGES</li></ul>
<h4 class="abs" style="left:883px;top:3398px;color:#fff;font-size:13px;font-weight:700;line-height:18px;font-family:Montserrat,sans-serif">SIGN UP TODAY TO PAY LESS<br>FOR YOUR ENERGY!</h4>
<p class="abs" style="left:883px;top:3452px;width:240px;color:#fff;font-size:10px;line-height:15px;opacity:.9">Each month we roll out numerous special offers and discounts on our solar panels.</p>
<div class="abs" style="left:883px;top:3498px;width:247px;height:18px;background:#fff;border-radius:10px"></div>
<div class="abs" style="left:0;top:3588px;width:1200px;border-top:1px solid rgba(255,255,255,.3)"></div>
<p class="abs" style="left:73px;top:3598px;color:#fff;font-size:9px">Sunward Energy © 2016 · Privacy Policy</p>
<div class="abs" style="left:1060px;top:3598px;display:flex;gap:8px"><i style="width:10px;height:10px;border-radius:50%;background:#fff;display:block"></i><i style="width:10px;height:10px;border-radius:50%;background:#fff;display:block"></i><i style="width:10px;height:10px;border-radius:50%;background:#fff;display:block"></i><i style="width:10px;height:10px;border-radius:50%;background:#fff;display:block"></i></div>

<div class="abs totop" style="left:1150px;top:464px"><svg width="12" height="8" viewBox="0 0 12 8"><path d="M1 7l5-5 5 5" stroke="#fff" stroke-width="2" fill="none"/></svg></div>
<div class="abs totop" style="left:1150px;top:672px"><svg width="12" height="8" viewBox="0 0 12 8"><path d="M1 7l5-5 5 5" stroke="#fff" stroke-width="2" fill="none"/></svg></div>
<div class="abs totop" style="left:1150px;top:1081px"><svg width="12" height="8" viewBox="0 0 12 8"><path d="M1 7l5-5 5 5" stroke="#fff" stroke-width="2" fill="none"/></svg></div>
<div class="abs totop" style="left:1150px;top:1490px;background:rgba(255,255,255,.25)"><svg width="12" height="8" viewBox="0 0 12 8"><path d="M1 7l5-5 5 5" stroke="#fff" stroke-width="2" fill="none"/></svg></div>
<div class="abs totop" style="left:1150px;top:1896px"><svg width="12" height="8" viewBox="0 0 12 8"><path d="M1 7l5-5 5 5" stroke="#fff" stroke-width="2" fill="none"/></svg></div>
<div class="abs totop" style="left:1150px;top:2307px"><svg width="12" height="8" viewBox="0 0 12 8"><path d="M1 7l5-5 5 5" stroke="#fff" stroke-width="2" fill="none"/></svg></div>
<div class="abs totop" style="left:1150px;top:2716px"><svg width="12" height="8" viewBox="0 0 12 8"><path d="M1 7l5-5 5 5" stroke="#fff" stroke-width="2" fill="none"/></svg></div>
<div class="abs totop" style="left:1150px;top:3125px"><svg width="12" height="8" viewBox="0 0 12 8"><path d="M1 7l5-5 5 5" stroke="#fff" stroke-width="2" fill="none"/></svg></div>
<div class="abs totop" style="left:1150px;top:3534px;background:rgba(255,255,255,.25)"><svg width="12" height="8" viewBox="0 0 12 8"><path d="M1 7l5-5 5 5" stroke="#fff" stroke-width="2" fill="none"/></svg></div>

</body>
</html>
```